Property Management Company Business Cards

Need business cards for a property management company located in Michigan. We manage houses for clients all over the world. Young and modern company, looking for eye catching design. Please work with the attached logo.

Industry/Entity Type

Property Management

Requirements
Must have
• Need lines for address, telephone number, fax number, web site.

Also lines for name, and job title

```html
<!DOCTYPE html>
<html lang="en">
<head>
<meta charset="utf-8">
<title>Larkfield Homes – Business Cards</title>
<link href="https://fonts.googleapis.com/css2?family=Open+Sans:wght@400;700;800&display=swap" rel="stylesheet">
<style>
  :root{
    --bg:#2b2b2d;
    --blue:#27a7e1;
    --blue-deep:#1b8fd0;
    --blue-light:#4fbdf0;
    --ink:#3a3b3d;
    --text:#2c2c2c;
    --rule:#9a9a9a;
    --paper:#f6f6f7;
    --white:#ffffff;
  }
  *{margin:0;padding:0;box-sizing:border-box}
  html,body{width:1200px;height:900px;overflow:hidden}
  body{
    background:var(--bg);
    font-family:"Open Sans",Arial,sans-serif;
    display:flex;flex-direction:column;align-items:center;justify-content:center;gap:56px;
  }
  .card{
    position:relative;width:630px;height:360px;overflow:hidden;
    box-shadow:0 14px 30px rgba(0,0,0,.45);
  }
  /* Front */
  .card--front{
    background:linear-gradient(135deg,var(--blue-light) 0%,var(--blue) 45%,var(--blue-deep) 100%);
    color:var(--white);
  }
  .front__tiles{position:absolute;inset:0}
  .front__brand{
    position:absolute;left:0;right:0;top:130px;
    display:flex;flex-direction:column;align-items:center;
  }
  .front__row{display:flex;align-items:center;gap:16px}
  .front__dot{width:30px;height:30px;border-radius:50%;background:var(--white)}
  .front__name{font-weight:800;font-size:40px;letter-spacing:.5px;line-height:1}
  .front__web{font-size:15px;margin-top:22px;padding-left:46px;letter-spacing:.5px}
  /* Back */
  .card--back{background:var(--paper);color:var(--text)}
  .back__deco{position:absolute;right:0;top:0;width:260px;height:360px}
  .back__brand{position:absolute;left:36px;top:52px;display:flex;align-items:center;gap:12px}
  .back__dot{width:26px;height:26px;border-radius:50%;background:var(--ink)}
  .back__name{font-weight:800;font-size:27px;color:var(--ink);line-height:1;letter-spacing:.3px}
  .person{position:absolute;left:36px;top:128px;width:260px}
  .person__name{font-weight:700;font-size:21px;color:var(--blue);letter-spacing:.5px;padding-bottom:6px;border-bottom:1px solid var(--rule)}
  .contact{position:absolute;left:0;width:400px;font-size:15px}
  .contact__line{display:flex;align-items:center;gap:7px;height:24px}
  .contact__line svg{width:14px;height:14px;fill:var(--blue);flex:none}
  .contact--top{top:180px;left:36px;display:flex;gap:22px}
  .contact--list{top:224px;padding-left:36px;border-top:1px solid var(--rule);padding-top:10px}
  .contact--addr{top:300px;padding-left:36px;border-top:1px solid var(--rule);padding-top:10px}
</style>
</head>
<body>

<section class="card card--front" aria-label="Business card front">
  <svg class="front__tiles" viewBox="0 0 630 360" aria-hidden="true">
    <rect x="40" y="40" width="90" height="70" fill="#fff" opacity=".06"/>
    <rect x="150" y="200" width="120" height="90" fill="#fff" opacity=".05"/>
    <rect x="440" y="30" width="110" height="80" fill="#fff" opacity=".07"/>
    <rect x="500" y="230" width="90" height="100" fill="#fff" opacity=".05"/>
    <rect x="300" y="10" width="70" height="60" fill="#fff" opacity=".04"/>
  </svg>
  <div class="front__brand">
    <div class="front__row">
      <span class="front__dot"></span>
      <span class="front__name">LARKFIELD HOMES</span>
    </div>
    <div class="front__web">www.larkfieldhomes.com</div>
  </div>
</section>

<section class="card card--back" aria-label="Business card back">
  <svg class="back__deco" viewBox="0 0 260 360" aria-hidden="true">
    <rect x="90" y="0" width="170" height="36" fill="var(--blue)"/>
    <rect x="150" y="36" width="110" height="264" fill="var(--ink)"/>
    <rect x="220" y="300" width="40" height="60" fill="var(--blue)"/>
  </svg>

  <div class="back__brand">
    <span class="back__dot"></span>
    <span class="back__name">LARKFIELD HOMES</span>
  </div>

  <div class="person"><div class="person__name">DANIEL WHITFIELD</div></div>

  <div class="contact contact--top">
    <div class="contact__line">
      <svg viewBox="0 0 16 16"><path d="M3 1l3 3-2 2c1 2 3 4 5 5l2-2 3 3-2 3C7 15 1 9 1 3z"/></svg>
      <span>555.010.2231</span>
    </div>
    <div class="contact__line">
      <svg viewBox="0 0 16 16"><path d="M4 1h8v4H4zM1 6h14v6h-3v3H4v-3H1zm4 4v4h6v-4z"/></svg>
      <span>555.010.2235</span>
    </div>
  </div>

  <div class="contact contact--list">
    <div class="contact__line">
      <svg viewBox="0 0 16 16"><path d="M1 3h14v10H1zm1 1v1l6 4 6-4V4z"/></svg>
      <span>daniel@larkfieldhomes.com</span>
    </div>
    <div class="contact__line">
      <svg viewBox="0 0 16 16"><path d="M8 1a7 7 0 100 14A7 7 0 008 1zm0 2a5 5 0 014.9 4H3.1A5 5 0 018 3zM3.1 9h9.8A5 5 0 013.1 9z"/></svg>
      <span>www.larkfieldhomes.com</span>
    </div>
  </div>

  <div class="contact contact--addr">
    <div class="contact__line">
      <svg viewBox="0 0 16 16"><path d="M8 1a4.5 4.5 0 00-4.5 4.5C3.5 9 8 13 8 13s4.5-4 4.5-7.5A4.5 4.5 0 008 1zm0 3a1.5 1.5 0 110 3 1.5 1.5 0 010-3zM3 14h10v1H3z"/></svg>
      <span>1420 Cedar Ln, Fairhaven, Michigan, 48000</span>
    </div>
  </div>
</section>

</body>
</html>
```